Dental Office Needs Exciting New Stationary

We need a stationary design that incorporates the logo that we already have and would like to keep the existing color scheme. We need something clean and professional. This is a Endodontic (root canals) office and must represent a dental specialist's office. I need a design for a business card, envelope, and letterhead that all coordinate. I would like the business card to incorporate the information in the business card sample that I am providing. I made the business card design myself but would like to see a better one.

```html
<!DOCTYPE html>
<html lang="en">
<head>
<meta charset="utf-8">
<title>Meridian Endodontics Stationery</title>
<link href="https://fonts.googleapis.com/css2?family=Montserrat:wght@500&family=Open+Sans:wght@400&display=swap" rel="stylesheet">
<style>
  :root {
    --backdrop: #d3dadf;
    --navy: #34406f;
    --navy-dark: #2b355f;
    --slate: #5e6064;
    --paper: #fbfbfb;
    --brand-blue: #2f7fc4;
    --brand-light: #7fb6e6;
    --ink: #6b6e73;
    --mark-grey: #b9bcc2;
    --shadow: 0 6px 14px rgba(40, 50, 70, 0.22);
  }
  * { box-sizing: border-box; margin: 0; padding: 0; }
  html, body { width: 1200px; height: 1000px; overflow: hidden; }
  body {
    background: var(--backdrop);
    font-family: "Open Sans", sans-serif;
    position: relative;
  }
  .piece { position: absolute; box-shadow: var(--shadow); overflow: hidden; }

  /* Brand name lockup */
  .brand { display: flex; align-items: center; gap: 6px; }
  .brand-dot { border-radius: 50%; background: var(--brand-blue); flex: none; }
  .brand-name {
    font-family: "Montserrat", sans-serif; font-weight: 500;
    color: var(--brand-blue); text-transform: uppercase; line-height: 1.05;
  }
  .brand-name span { display: block; }
  .on-dark .brand-dot { background: var(--brand-light); }
  .on-dark .brand-name { color: var(--brand-light); }

  .contact { font-size: 4.6px; color: var(--ink); line-height: 1.6; }
  .on-dark .contact { color: #d8dbe3; }

  /* Letterhead */
  .letterhead { left: 60px; top: 50px; width: 320px; height: 452px; background: var(--paper); padding: 30px 30px; }
  .letterhead .brand-dot { width: 14px; height: 14px; }
  .letterhead .brand-name { font-size: 9px; }
  .letter-body { margin-top: 26px; font-size: 5.4px; color: var(--ink); line-height: 1.7; }
  .letter-body p { margin-bottom: 10px; }
  .letter-sign { text-align: right; font-size: 5.4px; color: var(--ink); margin-top: 16px; }
  .signature { display: block; width: 64px; height: 12px; margin: 8px 18px 0 auto; background: #e2e4e8; border-radius: 2px; }
  .letterhead .contact { position: absolute; left: 30px; bottom: 26px; }
  .letter-accent { position: absolute; right: 22px; bottom: 40px; width: 58px; height: 58px; border-radius: 50%; background: #e7ebf3; }

  /* Envelopes */
  .envelope { width: 300px; height: 160px; background: var(--paper); }
  .envelope-open { left: 420px; top: 60px; }
  .envelope-open .flap { position: absolute; left: 0; top: 0; width: 100%; height: 42px; background: var(--navy); }
  .envelope-front { left: 760px; top: 60px; padding: 18px 20px; }
  .envelope-front .brand-dot { width: 12px; height: 12px; }
  .envelope-front .brand-name { font-size: 8px; }
  .envelope-front .contact { margin-top: 6px; margin-left: 18px; }
  .envelope-closed { left: 760px; top: 250px; }
  .envelope-closed .flap { position: absolute; left: 0; top: 0; width: 100%; height: 58px; background: var(--navy); display: flex; align-items: center; justify-content: center; }
  .envelope-closed .brand-dot { width: 9px; height: 9px; }
  .envelope-closed .brand-name { font-size: 6.5px; }

  /* Business cards */
  .card { top: 290px; width: 150px; height: 86px; background: var(--navy); }
  .card-front { left: 420px; display: flex; align-items: center; justify-content: center; }
  .card-front .brand-dot { width: 10px; height: 10px; }
  .card-front .brand-name { font-size: 6.5px; }
  .card-back { left: 590px; padding: 12px 12px; }
  .card-back .holder { font-family: "Montserrat", sans-serif; font-weight: 500; font-size: 6px; color: var(--brand-light); }
  .card-back .contact { margin-top: 3px; }
  .card-back .corner-dot { position: absolute; right: 10px; bottom: 9px; width: 8px; height: 8px; border-radius: 50%; background: var(--mark-grey); }
  .card-back .card-band { position: absolute; left: 0; bottom: 0; width: 100%; height: 22px; background: var(--slate); }

  /* Folder closed */
  .folder-cover { left: 60px; top: 530px; width: 330px; height: 420px; background: var(--navy); }
  .folder-cover .cover-brand { position: absolute; left: 50px; top: 120px; }
  .folder-cover .cover-brand .brand-dot { width: 34px; height: 34px; }
  .folder-cover .cover-brand .brand-name { font-size: 20px; }
  .folder-cover svg.cover-band { position: absolute; left: 0; bottom: 0; }
  .folder-cover .foot-brand { position: absolute; right: 18px; bottom: 40px; }
  .folder-cover .foot-brand .brand-dot { width: 12px; height: 12px; background: #e6e8ec; }
  .folder-cover .foot-brand .brand-name { font-size: 9px; color: #e6e8ec; }

  /* Folder open */
  .folder-open { left: 420px; top: 420px; width: 720px; height: 440px; background: var(--navy); }
  .folder-open .spine { position: absolute; left: 359px; top: 0; width: 2px; height: 100%; background: var(--navy-dark); }
  .pocket { position: absolute; bottom: 0; width: 340px; height: 170px; background: var(--slate); }
  .pocket-left { left: 10px; border-radius: 0 40px 0 0; }
  .pocket-right { left: 370px; height: 220px; border-radius: 40px 0 0 0; }
  .pocket-right .pocket-brand { position: absolute; right: 26px; top: 22px; }
  .pocket-right .brand-dot { width: 12px; height: 12px; }
  .pocket-right .brand-name { font-size: 8px; }
  .pocket-right .contact { position: absolute; right: 44px; top: 48px; width: 96px; }
</style>
</head>
<body>

  <!-- Letterhead -->
  <article class="piece letterhead">
    <div class="brand">
      <span class="brand-dot"></span>
      <div class="brand-name"><span>Meridian</span><span>Endodontics</span></div>
    </div>
    <div class="letter-body">
      <p>Dear Client</p>
      <p>We are pleased to welcome you to our practice and thank you for choosing us for your root canal care. Our team will review your records before your first visit.</p>
      <p>Please bring your referral letter, a list of current medications and your insurance card. Arrive ten minutes early so we can complete your intake forms.</p>
      <p>If you have questions about your treatment plan, call our front desk at any time. We look forward to seeing you soon.</p>
    </div>
    <div class="letter-sign">Best regards
      <span class="signature" role="img" aria-label="Handwritten signature of Elena Ward"></span>
    </div>
    <span class="letter-accent"></span>
    <div class="contact">
      1450 Harbor Avenue, Suite 200<br>
      Lakeview, OR 97630<br>
      (555) 014-2290<br>
      hello@meridianendo.com
    </div>
  </article>

  <!-- Envelopes -->
  <div class="piece envelope envelope-open"><div class="flap"></div></div>

  <div class="piece envelope envelope-front">
    <div class="brand">
      <span class="brand-dot"></span>
      <div class="brand-name"><span>Meridian</span><span>Endodontics</span></div>
    </div>
    <div class="contact">
      1450 Harbor Avenue, Suite 200<br>
      Lakeview, OR 97630<br>
      (555) 014-2290
    </div>
  </div>

  <div class="piece envelope envelope-closed">
    <div class="flap on-dark">
      <div class="brand">
        <span class="brand-dot"></span>
        <div class="brand-name"><span>Meridian</span><span>Endodontics</span></div>
      </div>
    </div>
  </div>

  <!-- Business cards -->
  <div class="piece card card-front on-dark">
    <div class="brand">
      <span class="brand-dot"></span>
      <div class="brand-name"><span>Meridian</span><span>Endodontics</span></div>
    </div>
  </div>

  <div class="piece card card-back on-dark">
    <div class="holder">Dr. Elena Ward</div>
    <div class="contact">
      Endodontist<br>
      (555) 014-2290<br>
      hello@meridianendo.com
    </div>
    <div class="card-band"></div>
    <span class="corner-dot"></span>
  </div>

  <!-- Presentation folder, closed -->
  <div class="piece folder-cover on-dark">
    <div class="brand cover-brand">
      <span class="brand-dot"></span>
      <div class="brand-name"><span>Meridian</span><span>Endodontics</span></div>
    </div>
    <svg class="cover-band" width="330" height="150" viewBox="0 0 330 150" aria-hidden="true">
      <path d="M0 70 Q220 60 330 0 L330 150 L0 150 Z" fill="var(--slate)"/>
    </svg>
    <div class="brand foot-brand">
      <span class="brand-dot"></span>
      <div class="brand-name"><span>Meridian</span><span>Endodontics</span></div>
    </div>
  </div>

  <!-- Presentation folder, open -->
  <div class="piece folder-open">
    <div class="spine"></div>
    <div class="pocket pocket-left"></div>
    <div class="pocket pocket-right on-dark">
      <div class="brand pocket-brand">
        <span class="brand-dot"></span>
        <div class="brand-name"><span>Meridian</span><span>Endodontics</span></div>
      </div>
      <div class="contact">
        1450 Harbor Avenue, Suite 200<br>
        Lakeview, OR 97630<br>
        (555) 014-2290
      </div>
    </div>
  </div>

</body>
</html>
```